Label for kTw Ranch beef tallow

I need a small label to go on a 2oz amber glass jar as well as a 4 oz. amber glass jar of moisturizer.
I prefer it to be rectangular for the 2oz jar since it's small and square for the 4oz jar.
I'd like to keep our kTw Ranch logo the same font and style, which is attached. Ten Sleep, Wyoming should be left out. The font for kTw Ranch is spartan.
The label content is as follows:
Meadowlark Balm
Whipped Moisturizer
Ingredients: Beef Tallow, jojoba oil, peppermint oil.
2oz. jar

Instead of a white label, I'm thinking of a tan or brown label that will blend in with the amber jar. The lettering could then be a white, cream or even rust/burgandy color. Something to give it a rich look.

Thank you!

Target Market(s)

Mainly women but men as well.

Industry/Entity Type

Ranching and online beef sales

Requirements
Must have
• kTw Ranch logo

```html
<!DOCTYPE html>
<html lang="en">
<head>
<meta charset="utf-8">
<title>kTw Ranch – Meadowlark Balm Labels</title>
<link rel="stylesheet" href="https://fonts.googleapis.com/css2?family=Bebas+Neue&family=Josefin+Sans:wght@400;600;700&display=swap">
<style>
  :root {
    --backdrop: #8f8f8f;
    --label-brown: #5a3815;
    --cream: #dcc4a8;
    --white: #ffffff;
    --shadow: rgba(0, 0, 0, 0.35);
  }
  * { margin: 0; padding: 0; box-sizing: border-box; }
  html, body {
    width: 1200px;
    height: 584px;
    overflow: hidden;
    background: var(--backdrop);
  }
  .sheet {
    position: relative;
    width: 1200px;
    height: 584px;
  }
  .label {
    position: absolute;
    width: 516px;
    background: var(--label-brown);
    box-shadow: 10px 10px 12px var(--shadow);
    color: var(--white);
  }
  .label--rect { left: 60px; top: 138px; height: 297px; }
  .label--square { left: 625px; top: 65px; height: 444px; }

  .row {
    position: absolute;
    left: 0;
    right: 0;
    text-align: center;
    line-height: 1;
  }

  .brand-name {
    font-family: "Josefin Sans", sans-serif;
    font-weight: 400;
    color: var(--white);
    letter-spacing: 0.08em;
    white-space: nowrap;
  }

  .product-name {
    font-family: "Bebas Neue", sans-serif;
    font-weight: 400;
    color: var(--cream);
    font-size: 66px;
    letter-spacing: 3px;
    white-space: nowrap;
  }

  .product-type {
    display: flex;
    align-items: center;
    justify-content: center;
    font-family: "Josefin Sans", sans-serif;
    font-weight: 600;
    font-size: 16px;
    letter-spacing: 0.3em;
    white-space: nowrap;
  }
  .product-type .rule {
    display: block;
    width: 52px;
    height: 1.5px;
    background: var(--white);
  }
  .product-type .text { padding: 0 4px 0 6px; margin-right: -0.3em; }

  .ingredients-tag {
    display: inline-block;
    width: 130px;
    height: 20px;
    background: var(--white);
    color: var(--label-brown);
    clip-path: polygon(0 0, 100% 0, 96% 50%, 100% 100%, 0 100%, 4% 50%);
    font-family: "Josefin Sans", sans-serif;
    font-weight: 700;
    font-size: 15px;
    line-height: 23px;
  }

  .ingredients-list {
    font-family: "Josefin Sans", sans-serif;
    font-weight: 400;
    font-size: 11.5px;
    letter-spacing: 0.02em;
  }

  .net-weight {
    font-family: "Josefin Sans", sans-serif;
    font-weight: 600;
    color: var(--cream);
  }

  /* rectangular 2oz label */
  .label--rect .brand-name { top: 44px; font-size: 28px; }
  .label--rect .product-name { top: 106px; }
  .label--rect .product-type { top: 166px; }
  .label--rect .tag-row { top: 201px; }
  .label--rect .ingredients-list { top: 229px; }
  .label--rect .net-weight { top: 262px; font-size: 20px; }

  /* square 4oz label */
  .label--square .brand-name { top: 100px; font-size: 60px; }
  .label--square .product-name { top: 224px; }
  .label--square .product-type { top: 284px; }
  .label--square .tag-row { top: 323px; }
  .label--square .ingredients-list { top: 353px; }
  .label--square .net-weight { top: 399px; font-size: 27px; }
</style>
</head>
<body>
<main class="sheet">

  <section class="label label--rect" aria-label="2oz jar label">
    <div class="row brand-name">KTW RANCH</div>
    <h1 class="row product-name">MEADOWLARK BALM</h1>
    <p class="row product-type"><span class="rule"></span><span class="text">WHIPPED MOISTURIZER</span><span class="rule"></span></p>
    <div class="row tag-row"><span class="ingredients-tag">INGREDIENTS</span></div>
    <p class="row ingredients-list">BEEF TALLOW, JOJOBA OIL, PEPPERMINT OIL.</p>
    <p class="row net-weight">2oz.</p>
  </section>

  <section class="label label--square" aria-label="4oz jar label">
    <div class="row brand-name">KTW RANCH</div>
    <h2 class="row product-name">MEADOWLARK BALM</h2>
    <p class="row product-type"><span class="rule"></span><span class="text">WHIPPED MOISTURIZER</span><span class="rule"></span></p>
    <div class="row tag-row"><span class="ingredients-tag">INGREDIENTS</span></div>
    <p class="row ingredients-list">BEEF TALLOW, JOJOBA OIL, PEPPERMINT OIL.</p>
    <p class="row net-weight">4oz.</p>
  </section>

</main>
</body>
</html>
```